Obrelo Business Card

Need a double sided business card. Would like the business card to have the logo on one side and the employees details and business contact details on the other.

Business

```html
<!DOCTYPE html>
<html lang="en">
<head>
<meta charset="utf-8">
<title>Obrelo Business Card</title>
<link rel="stylesheet" href="https://fonts.googleapis.com/css2?family=Open+Sans:wght@400;600;700&display=swap">
<style>
  :root {
    --backdrop: #262626;
    --card: #fbfbfb;
    --lime: #a6cf4c;
    --ink: #2b2b2b;
    --slate: #7d868c;
    --rule: #cfd9b4;
  }
  * { margin: 0; padding: 0; box-sizing: border-box; }
  html, body {
    width: 1200px; height: 722px; overflow: hidden;
    background: var(--backdrop);
    font-family: "Open Sans", Arial, sans-serif;
  }
  .stage {
    position: relative; width: 1200px; height: 722px;
  }
  .card {
    position: absolute; top: 206px;
    width: 540px; height: 310px;
    background: var(--card);
    overflow: hidden;
  }
  .card--front { left: 40px; }
  .card--back { left: 620px; }

  .band { position: absolute; background: var(--lime); }

  .wordmark {
    position: absolute;
    font-family: "Open Sans", Arial, sans-serif;
    font-weight: 700;
    color: var(--lime);
    letter-spacing: -1px;
    line-height: 1;
  }

  /* Front */
  .card--front .band--left { left: 0; top: 165px; width: 190px; height: 90px; }
  .card--front .band--right { left: 450px; top: 150px; width: 90px; height: 90px; }
  .card--front .wordmark { left: 56px; top: 100px; font-size: 46px; }

  .person {
    position: absolute; left: 205px; top: 183px; width: 118px;
    text-align: right;
  }
  .person__name { font-size: 14px; font-weight: 700; color: var(--ink); }
  .person__role { font-size: 14px; font-weight: 700; color: var(--lime); margin-top: 2px; }
  .divider {
    position: absolute; left: 333px; top: 168px; width: 1px; height: 80px;
    background: var(--rule);
  }
  .contact {
    position: absolute; left: 340px; top: 163px; width: 88px;
    text-align: right; list-style: none;
    font-size: 10.5px; line-height: 15px; color: var(--ink);
  }
  .contact-icons {
    position: absolute; left: 432px; top: 160px;
  }

  /* Back */
  .card--back .band--left { left: 0; top: 170px; width: 255px; height: 90px; }
  .card--back .band--right { left: 455px; top: 118px; width: 85px; height: 88px; }
  .card--back .wordmark { left: 268px; top: 168px; font-size: 44px; }
</style>
</head>
<body>
<main class="stage">
  <section class="card card--front" aria-label="Business card front">
    <div class="band band--left"></div>
    <div class="band band--right"></div>
    <div class="wordmark">obrelo</div>
    <div class="person">
      <p class="person__name">Employee Name</p>
      <p class="person__role">Manager</p>
    </div>
    <div class="divider"></div>
    <ul class="contact">
      <li>Address line 1</li>
      <li>Address line 2</li>
      <li>00000000002</li>
      <li>email@email.com</li>
      <li>www.website.com</li>
    </ul>
    <svg class="contact-icons" width="14" height="80" viewBox="0 0 14 80" aria-hidden="true">
      <g fill="none" stroke="#a6cf4c" stroke-width="1.6">
        <path d="M7 14 C3 9 2.5 7 2.5 5.5 A4.5 4.5 0 0 1 11.5 5.5 C11.5 7 11 9 7 14 Z" fill="#a6cf4c"/>
        <circle cx="7" cy="5.5" r="1.6" fill="#fbfbfb" stroke="none"/>
        <rect x="3" y="25" width="8" height="11" rx="1.5"/>
        <line x1="6" y1="33.5" x2="8" y2="33.5"/>
        <rect x="1.5" y="46" width="11" height="8" rx="1"/>
        <path d="M1.5 46.5 L7 51 L12.5 46.5"/>
        <circle cx="7" cy="69" r="5.5"/>
        <ellipse cx="7" cy="69" rx="2.3" ry="5.5"/>
        <line x1="1.5" y1="69" x2="12.5" y2="69"/>
      </g>
    </svg>
  </section>

  <section class="card card--back" aria-label="Business card back">
    <div class="band band--left"></div>
    <div class="band band--right"></div>
    <div class="wordmark">obrelo</div>
  </section>
</main>
</body>
</html>
```